Postcard Design

Heating & Cooling

I want to create a post card for a Tune Up program that we offer customer for this spring.
Updates

I would like to change the date from April 1st - June 31st.
I would also like to change the size and go larger for the post card.

Keep the designs coming.
Thanks

I have decided to change the price of the cost of the program to "Only $99.00" due to other competitors pricing in my area.
If possible include at the bottom of the design > "Does not cover repair or parts" in a small font

Reason: We need more time for better designs. So I am extending the deadline by 7 days.

Target Market(s)

Residential Customers for Air Conditioning Tune Ups

Requirements
Must have
• We are promoting a tune up for the air conditioning system for $129.00.

The price is effective from April 1st - July 31st

I would like for the post card to be attention grabbing from the customers point of view. So mainly, add bold letting and everything to get attention.
Nice to have
• Also add to the card if possible:
Lower Energy Bills
Increase the life of your system
Prevent future breakdowns

Stay Cool this Summer with our Brightvale Tune Up Program

And add a logo that shows stacks of coins to indicate the money that can be saved

You also can look at other post cards that has been created for this particular program and design from it.

```html
<!DOCTYPE html>
<html lang="en">
<head>
<meta charset="utf-8">
<title>Brightvale Tune-Up Postcard</title>
<link href="https://fonts.googleapis.com/css2?family=Open+Sans:wght@400;700;800&display=swap" rel="stylesheet">
<style>
  :root {
    --ink: #111111;
    --navy: #1e2440;
    --navy-deep: #20263f;
    --periwinkle: #6b73ba;
    --badge-blue: #4b5ba9;
    --red: #b0252a;
    --white: #ffffff;
    --frame: #2a2f45;
  }
  * { margin: 0; padding: 0; box-sizing: border-box; }
  html, body { width: 1200px; height: 930px; overflow: hidden; background: var(--white); }
  body { font-family: "Open Sans", Verdana, sans-serif; }
  .postcard { position: relative; width: 1200px; height: 930px; background: var(--white); overflow: hidden; }

  .program-name { position: absolute; left: 58px; top: 14px; color: var(--ink); font-weight: 800; font-size: 96px; letter-spacing: -2px; line-height: 1; }
  .program-sub { position: absolute; left: 272px; top: 122px; color: var(--ink); font-weight: 800; font-size: 50px; line-height: 1; letter-spacing: -1px; }

  .headline { position: absolute; left: 28px; top: 192px; color: var(--navy); font-weight: 800; font-size: 36px; line-height: 47px; }
  .tagline { position: absolute; left: 30px; top: 299px; color: var(--navy); font-weight: 700; font-size: 24px; }

  .coins-photo { position: absolute; left: 932px; top: 101px; width: 232px; height: 223px; border: 2px solid var(--frame);
    background: radial-gradient(ellipse at 55% 60%, #e4b33c 0%, #c48a1c 45%, #f4f1ea 80%); }
  .price-badge { position: absolute; left: 802px; top: 35px; width: 192px; height: 192px; border-radius: 50%; background: var(--badge-blue);
    display: flex; align-items: center; justify-content: center; color: var(--white); font-weight: 800; font-size: 34px; }
  .price-badge span { transform: rotate(-15deg); }

  .stripe-navy { position: absolute; left: 0; top: 347px; width: 1200px; height: 12px; background: var(--navy-deep); }
  .stripe-red { position: absolute; left: 0; top: 368px; width: 1200px; height: 13px; background: var(--red); }

  .lower-panel { position: absolute; left: 0; top: 392px; width: 1200px; height: 538px;
    background: linear-gradient(90deg, var(--navy-deep) 0%, #3a4170 45%, var(--periwinkle) 100%); }

  .tech-photo { position: absolute; left: 20px; top: 443px; width: 555px; height: 430px; border: 3px solid #e8e8ee;
    background: linear-gradient(135deg, #8a4a38 0%, #9c5a44 40%, #7d7f85 65%, #5a4a38 100%); }

  .benefits { position: absolute; left: 622px; top: 444px; list-style: none; }
  .benefits li { display: flex; align-items: center; height: 71px; color: var(--white); font-weight: 700; font-size: 28px; }
  .benefits svg { width: 26px; height: 24px; margin-right: 20px; }

  .offer-dates { position: absolute; left: 672px; top: 661px; width: 407px; height: 97px; background: var(--red);
    color: var(--white); font-weight: 700; font-size: 24px; line-height: 33px; padding: 15px 0 0 24px; }

  .fine-print { position: absolute; left: 652px; top: 838px; color: var(--white); font-size: 22px; }

  .company-name { position: absolute; left: 1030px; top: 820px; width: 160px; color: var(--white); font-weight: 800; font-size: 19px; line-height: 23px; }
</style>
</head>
<body>
<main class="postcard">
  <div class="program-name">Brightvale</div>
  <div class="program-sub">Tune-Up</div>

  <h1 class="headline">We are promoting a tune up<br>for the air conditioning system for $99.00</h1>
  <p class="tagline">Stay Cool this Summer with our Brightvale Tune Up Program</p>

  <div class="coins-photo" role="img" aria-label="Photo of stacks of gold coins"></div>
  <div class="price-badge"><span>$99.00</span></div>

  <div class="stripe-navy"></div>
  <div class="stripe-red"></div>

  <section class="lower-panel"></section>
  <div class="tech-photo" role="img" aria-label="Photo of a technician servicing an outdoor air conditioning unit beside a brick wall"></div>

  <ul class="benefits">
    <li><svg viewBox="0 0 26 24"><path d="M2 13 L9 20 L24 3" fill="none" stroke="#c8282c" stroke-width="4" stroke-linecap="round" stroke-linejoin="round"/></svg>Lower Energy Bills</li>
    <li><svg viewBox="0 0 26 24"><path d="M2 13 L9 20 L24 3" fill="none" stroke="#c8282c" stroke-width="4" stroke-linecap="round" stroke-linejoin="round"/></svg>Increase the life of your system</li>
    <li><svg viewBox="0 0 26 24"><path d="M2 13 L9 20 L24 3" fill="none" stroke="#c8282c" stroke-width="4" stroke-linecap="round" stroke-linejoin="round"/></svg>Prevent future breakdowns</li>
  </ul>

  <div class="offer-dates">The price is effective<br>from April 1st - June 31st</div>

  <p class="fine-print">Does not cover repair or parts</p>
  <div class="company-name">Northgate Heating &amp; Cooling</div>
</main>
</body>
</html>
```